we are a college and require a design of a printable graduation certificate

our courses range from certicate III to Diploma

We would a high quality design, similar to a unveristy degree, so its meaning full to the students and looks great on the wall

our college website is: www.marlowinstitute.example.au

Industry/Entity Type

College

Requirements
Must have
• security feature like water mark or stamp

```html
<!DOCTYPE html>
<html lang="en">
<head>
<meta charset="utf-8">
<title>Marlow Institute Graduation Certificate</title>
<link rel="stylesheet" href="https://fonts.googleapis.com/css2?family=Cormorant+Infant:ital,wght@1,600&family=PT+Sans:ital,wght@0,400;0,700;1,400&display=swap">
<style>
  :root {
    --backdrop: #e9edf3;
    --paper: #eef6fc;
    --border-light: #c9d3f1;
    --border-deep: #6f7fd0;
    --frame: #3f4fb0;
    --ink: #1c1c22;
    --script-blue: #2a86cc;
    --seal-blue: #2d5aa8;
    --watermark: #b8c6ea;
  }
  * { box-sizing: border-box; margin: 0; padding: 0; }
  html, body {
    width: 1200px; height: 900px; overflow: hidden;
    background: var(--backdrop);
  }
  .certificate {
    position: absolute; left: 70px; top: 70px;
    width: 1060px; height: 760px;
    background: var(--paper);
    font-family: "PT Sans", Arial, sans-serif;
    color: var(--ink);
  }
  .guilloche-border {
    position: absolute; inset: 14px;
    border-radius: 4px;
    background: linear-gradient(135deg, var(--border-light), var(--border-deep) 50%, var(--border-light));
  }
  .inner-panel {
    position: absolute; inset: 58px;
    background: var(--paper);
    border: 3px solid var(--frame);
    outline: 1px solid var(--frame);
    outline-offset: 4px;
  }
  .security-watermark {
    position: absolute; left: 380px; top: 180px;
    width: 300px; height: 300px;
    transform: rotate(45deg);
    background: radial-gradient(circle, rgba(184,198,234,.75) 0%, rgba(184,198,234,.35) 55%, rgba(184,198,234,.15) 100%);
  }
  .institute-mark {
    position: absolute; left: 0; right: 0; top: 96px;
    display: flex; flex-direction: column; align-items: center; gap: 12px;
  }
  .institute-mark .seal {
    width: 62px; height: 62px; border-radius: 50%;
    background: var(--seal-blue);
  }
  .institute-mark .institute-name {
    font-weight: 700; font-size: 22px; letter-spacing: .04em;
    text-transform: uppercase; color: var(--seal-blue);
  }
  .issue-date, .record-details {
    position: absolute; font-style: italic; font-size: 13px; line-height: 19px;
  }
  .issue-date { left: 112px; top: 176px; }
  .record-details { left: 700px; top: 132px; }
  .certify-line {
    position: absolute; left: 122px; top: 232px; font-size: 15px;
  }
  .graduate-name {
    position: absolute; left: 0; right: 0; top: 258px;
    text-align: center;
    font-family: "Cormorant Infant", Georgia, serif;
    font-style: italic; font-weight: 600;
    font-size: 86px; line-height: 1; word-spacing: 18px;
    color: var(--script-blue);
  }
  .citation {
    position: absolute; left: 138px; top: 382px; width: 790px;
    font-style: italic; font-size: 15.5px; line-height: 25px;
  }
  .compliance {
    position: absolute; left: 146px; top: 502px;
    font-style: italic; font-size: 14px;
  }
  .signatory { position: absolute; text-align: center; }
  .signatory .printed-name {
    font-family: "Cormorant Infant", Georgia, serif;
    font-style: italic; font-weight: 600;
    font-size: 28px; color: var(--script-blue); word-spacing: 6px;
  }
  .signatory .role { font-size: 14px; }
  .signatory .signature {
    margin: 6px auto 0; width: 110px; height: 26px;
    background: linear-gradient(90deg, rgba(28,28,34,.25), rgba(28,28,34,.55), rgba(28,28,34,.25));
    border-radius: 13px;
  }
  .signatory.chair { left: 168px; top: 548px; width: 160px; }
  .signatory.president { left: 690px; top: 512px; width: 180px; }
</style>
</head>
<body>
  <main class="certificate">
    <div class="guilloche-border" role="img" aria-label="Fine blue guilloche wave border"></div>
    <section class="inner-panel"></section>
    <div class="security-watermark" role="img" aria-label="Faint guilloche rosette security watermark"></div>

    <header class="institute-mark">
      <span class="seal"></span>
      <span class="institute-name">Marlow Institute</span>
    </header>

    <p class="issue-date">Given under our hand in this day<br>October 13, 2009</p>
    <p class="record-details">Certificate number : 00421<br>Date of Expiration : &nbsp;October 31, 2011</p>

    <p class="certify-line">This to certify that</p>
    <h1 class="graduate-name">Jordan Avery</h1>

    <p class="citation">Lorem ipsum dolor sit amet, consectetur adipiscing elit. Nulla accumsan commodo lorem, id iaculis eros volutpat ut. Nulla facilisi. Cras quis posuere turpis. Nulla facilisi. Aenean massa libero, accumsan sed luctus a, hendrerit sed arcu. Integer est nisl, placerat att sollicitudin id, elementum sit amet nisi. Mauris sollicitudin elit ut dui pellentesque ullamcorper. Donec auctor feugiat gravida. Nunc ac libero sed nibh rutrum convallis nec sit amet nulla.</p>

    <p class="compliance">Issued in accordance with ORGANISE administrative rules and guidlines.</p>

    <div class="signatory chair">
      <p class="printed-name">Elias Moore</p>
      <p class="role">Certification Chairman</p>
      <div class="signature" role="img" aria-label="Handwritten signature of the certification chairman"></div>
    </div>

    <div class="signatory president">
      <p class="printed-name">Helena Park</p>
      <p class="role">Company president</p>
      <div class="signature" role="img" aria-label="Handwritten signature of the company president"></div>
    </div>
  </main>
</body>
</html>
```